Wordpress Design Project for Employee Communications Site

We need a Wordpress design for a company that strategizes on and produces materials for employee communications. Improving employee communications at all levels of an organization can help improve overall company performance and results. The site needs to look very clean and professional; we're not afraid of white space. We like the functionality that Wordpress provides; however, we only want one "true" blog page; the other pages should give the impression of a more "static" web site - particularly the home page. I have a logo that I can provide.

I have added these comments to the discussion page:
Great question - thank you for asking it. I’ve done more research

I like the very clean and monochromatic looks to many of these. I don’t have to have monochromatic, but I do like minimal colors. Simple, clean, organized. The home page should “fit” almost entirely without scrolling. I do like fat footers that you can scroll down to. I don’t want a colored background, but any that I’ve chosen with colored backgrounds could be switched to a white background.

http://www.moravelkinst.com/
http://pondrix.com/
http://v1.belmarquist.com/
http://howtheotter.com/
http://stayingnimble.com/
http://www.interiors.pelmun.co.uk/
http://brixalumnihub.com/

These last two are more corporate sites. The first one is from a well-respected consultant in my area who does a lot of what I do. And I think Harwick does a nice job with their site. So, I want to marry the look I like with getting the content job done.

http://www.messagefuelworks.com/
http://www.harwick.com/view/en_US/us/index.htm

Target Market(s)

Target market is mid- to large-sized companies. More than 500 employees.

Industry/Entity Type

Communications

Requirements
Must have
• Need an impactful home page. There should be a "blog" page; contact us; services; about. For starters, at least. I want fonts to be very readable - that is, either quite dark gray or black.
Nice to have
• I am loathe to include a picture of myself, but I do want some images that say, "professional" and "expert" in communications.
Should not have
• I don't want a hits counter :) (I know no one would do that!).

```html
<!DOCTYPE html>
<html lang="en">
<head>
<meta charset="utf-8">
<title>Veriton Communications Company — Works</title>
<link rel="stylesheet" href="https://fonts.googleapis.com/css2?family=Maven+Pro:wght@400;500;700&family=Cabin:ital,wght@0,400;0,600;1,400;1,700&family=PT+Serif&display=swap">
<style>
  :root {
    --green: #bfd730;
    --blue: #29abe2;
    --ink: #3a3a3a;
    --text: #444;
    --muted: #666;
    --rule: #8a8a8a;
    --footer-bg: #f2f2f2;
    --olive: #8aa400;
    --photo-dark: #2b3a55;
    --square: #b5b5b5;
  }
  * { box-sizing: border-box; margin: 0; padding: 0; }
  html, body { width: 936px; height: 1200px; overflow: hidden; background: #fff; }
  body { position: relative; font-family: "Cabin", sans-serif; color: var(--text); }

  .brand { position: absolute; left: 66px; top: 30px; display: flex; align-items: center; gap: 12px; }
  .brand-mark { width: 26px; height: 26px; background: var(--square); }
  .brand-name { font-family: "Maven Pro", sans-serif; font-weight: 500; color: var(--ink); font-size: 34px; line-height: 1; }
  .brand-full { position: absolute; left: 70px; top: 71px; font-family: "Maven Pro", sans-serif; font-weight: 500; font-size: 12px; color: var(--ink); }

  .nav-rule { position: absolute; top: 99px; height: 3px; background: var(--rule); }
  .nav-rule.left { left: 0; width: 520px; }
  .nav-rule.right { left: 812px; width: 124px; }
  .main-nav { position: absolute; top: 90px; left: 527px; display: flex; font-family: "Maven Pro", sans-serif; font-size: 16px; }
  .main-nav a { color: var(--ink); text-decoration: none; padding: 0 13px; border-left: 1px solid var(--ink); line-height: 18px; }
  .main-nav a:first-child { border-left: 0; padding-left: 0; color: var(--blue); position: relative; }
  .main-nav a:first-child::after { content: ""; position: absolute; left: 17px; top: 19px; width: 5px; height: 5px; border-right: 1.5px solid var(--blue); border-bottom: 1.5px solid var(--blue); transform: rotate(45deg); }

  .hero { position: absolute; left: 59px; top: 126px; width: 816px; height: 174px; border: 1px solid #e3e3e3; }
  .hero-text { position: absolute; left: 5px; top: 5px; width: 281px; height: 162px; background: var(--green); padding: 10px 11px; font-family: "Maven Pro", sans-serif; font-size: 22px; line-height: 27.5px; color: #333; }
  .hero-text strong { color: #fff; font-weight: 700; }
  .hero-photo { position: absolute; left: 291px; top: 5px; width: 520px; height: 162px; background: linear-gradient(90deg, #e9ecef, #cfd5dc 50%, #8e98a5); }

  .post { position: absolute; left: 0; width: 936px; height: 320px; }
  .post-date { position: absolute; left: 54px; top: 0; }
  .post-date .date { position: absolute; left: 12px; top: 12px; width: 56px; text-align: center; font-family: "PT Serif", serif; color: #fff; font-size: 15px; line-height: 15px; }
  .post-title { position: absolute; left: 145px; top: 8px; font-family: "Maven Pro", sans-serif; font-weight: 400; font-size: 17px; color: #555; }
  .post-meta { position: absolute; left: 151px; top: 45px; font-size: 10px; display: flex; align-items: center; gap: 14px; }
  .post-meta .author { color: var(--olive); }
  .post-meta .sep { color: var(--muted); }
  .post-meta .comments { color: var(--muted); display: flex; align-items: center; gap: 7px; }
  .post-media { position: absolute; left: 64px; top: 96px; width: 223px; height: 165px; background: #f4f4f4; padding: 4px; }
  .post-media .photo { width: 214px; height: 142px; background: radial-gradient(circle at 40% 30%, #6f9fd8, var(--photo-dark) 70%); }
  .post-body { position: absolute; left: 305px; top: 106px; width: 568px; font-size: 9.4px; line-height: 15.3px; color: var(--text); }
  .post-body p + p { margin-top: 13px; }
  .post-body em { font-weight: 700; color: #333; }
  .read-more { position: absolute; left: 307px; top: 276px; font-size: 10px; font-style: italic; color: var(--blue); text-decoration: underline; }
  .share { position: absolute; left: 757px; top: 270px; display: flex; gap: 6px; }
  .share span { display: flex; align-items: center; gap: 4px; height: 19px; padding: 0 6px; font-size: 8px; border-radius: 2px; }
  .share .fb { width: 58px; background: #3b5998; color: #fff; }
  .share .tw { width: 56px; background: #eef6fb; border: 1px solid #c6dcea; color: #2a7fb8; font-size: 11px; }
  .share i { width: 9px; height: 9px; background: currentColor; display: block; opacity: .8; }
  .post-divider { position: absolute; left: 85px; top: 305px; width: 792px; border-top: 2px dotted #ddd; }

  .site-footer { position: absolute; left: 0; top: 1017px; width: 936px; height: 146px; background: var(--footer-bg); border-top: 1px solid #e6e6e6; }
  .footer-col { position: absolute; top: 10px; height: 117px; }
  .footer-col h4 { font-family: "Maven Pro", sans-serif; font-size: 11.5px; font-weight: 700; color: #333; margin-top: 4px; margin-bottom: 7px; }
  .footer-col li { list-style: none; font-size: 8.8px; letter-spacing: .3px; line-height: 15.3px; color: #444; }
  .footer-col.divided { border-right: 1px solid #ccc; }
  .social { display: flex; gap: 5px; }
  .social span { width: 13px; height: 13px; background: #6b8fb8; display: block; }
  .copyright { position: absolute; top: 1174px; left: 0; width: 936px; text-align: center; font-size: 9px; color: #444; letter-spacing: .2px; }
</style>
</head>
<body>

<header>
  <div class="brand"><span class="brand-mark"></span><span class="brand-name">Veriton</span></div>
  <div class="brand-full">Veriton Communications Company</div>
  <div class="nav-rule left"></div>
  <nav class="main-nav">
    <a href="#">works</a><a href="#">process</a><a href="#">about</a><a href="#">contact</a>
  </nav>
  <div class="nav-rule right"></div>
</header>

<section class="hero">
  <div class="hero-text">We help <strong>businesses improve</strong> their performance through effective communication. Our approach is simple</div>
  <div class="hero-photo" role="img" aria-label="Photo of business colleagues talking together in a bright office"></div>
</section>

<article class="post" style="top:350px">
  <div class="post-date">
    <svg width="80" height="76" viewBox="0 0 80 76"><rect x="0" y="0" width="80" height="3" fill="#e5e5e5"/><path d="M12 3h56v70L40 51 12 73z" fill="var(--blue)"/></svg>
    <div class="date">AUG<br>10</div>
  </div>
  <h2 class="post-title">Organizational and Business Communications</h2>
  <div class="post-meta"><span class="author">Posted by Marlowen</span><span class="sep">|</span><span class="comments">2 Comments
    <svg width="14" height="12" viewBox="0 0 14 12"><path d="M1 1h12v7H6l-3 3V8H1z" fill="none" stroke="#999"/></svg></span></div>
  <div class="post-media"><div class="photo" role="img" aria-label="Photo of a businessman in a suit on a stage under blue lights"></div></div>
  <div class="post-body">
    <p><em>Here is a brief exercise that I used in teaching nonverbal communication and that I rewrote for a textbook in nonverbal that I’m in the process of writing. Here I use it as an introduction to the discussion</em> of height but it can also be used with perception, stereotypes, and media influences, for example. You can adjust it in any way you’d like for your own classes.</p>
    <p>Workplace Message Digest: Find out what’s going on in the world of corporate and business communications.<br>Nora Belcastle: This consultant and expert offers insight into business and organizational communications.<br>Signal Undertones: Learn about using communications to better communicate within your organization, and with others outside your organization.<br>Clearer Dialogue Outcomes: This Aussie knows how to communicate more effectively in business settings.<br>Boardroom Lens: This blog is meant for corporate communications professionals.</p>
  </div>
  <a class="read-more">Contineue Reading</a>
  <div class="share"><span class="fb"><i></i>SHARE</span><span class="tw"><i></i>Post</span></div>
  <div class="post-divider"></div>
</article>

<article class="post" style="top:678px">
  <div class="post-date">
    <svg width="80" height="76" viewBox="0 0 80 76"><rect x="0" y="0" width="80" height="3" fill="#e5e5e5"/><path d="M12 3h56v70L40 51 12 73z" fill="var(--blue)"/></svg>
    <div class="date">AUG<br>10</div>
  </div>
  <h2 class="post-title">Organizational and Business Communications</h2>
  <div class="post-meta"><span class="author">Posted by Marlowen</span><span class="sep">|</span><span class="comments">2 Comments
    <svg width="14" height="12" viewBox="0 0 14 12"><path d="M1 1h12v7H6l-3 3V8H1z" fill="none" stroke="#999"/></svg></span></div>
  <div class="post-media" style="top:88px"><div class="photo" role="img" aria-label="Photo of a businessman in a suit on a stage under blue lights"></div></div>
  <div class="post-body" style="top:98px">
    <p><em>Here is a brief exercise that I used in teaching nonverbal communication and that I rewrote for a textbook in nonverbal that I’m in the process of writing. Here I use it as an introduction to the discussion</em> of height but it can also be used with perception, stereotypes, and media influences, for example. You can adjust it in any way you’d like for your own classes.</p>
    <p>Workplace Message Digest: Find out what’s going on in the world of corporate and business communications.<br>Nora Belcastle: This consultant and expert offers insight into business and organizational communications.<br>Signal Undertones: Learn about using communications to better communicate within your organization, and with others outside your organization.<br>Clearer Dialogue Outcomes: This Aussie knows how to communicate more effectively in business settings.<br>Boardroom Lens: This blog is meant for corporate communications professionals.</p>
  </div>
  <a class="read-more" style="top:268px">Contineue Reading</a>
  <div class="share" style="top:262px"><span class="fb"><i></i>SHARE</span><span class="tw"><i></i>Post</span></div>
  <div class="post-divider" style="top:295px"></div>
</article>

<footer class="site-footer">
  <div class="footer-col divided" style="left:82px;width:110px">
    <h4>Company</h4>
    <ul><li>About Us</li><li>Sitemap</li><li>Website Terms</li><li>Terms of Business</li><li>Privacy Policy</li></ul>
  </div>
  <div class="footer-col divided" style="left:238px;width:116px">
    <h4>Product</h4>
    <ul><li>Business Websites</li><li>Reviews</li><li>Quick Tour</li><li>Pricing</li><li>Free Trial</li></ul>
  </div>
  <div class="footer-col divided" style="left:395px;width:136px">
    <h4>Internet Marketing</h4>
    <ul><li>Marketing Tips</li><li>Search Optimisation</li><li>Social Media</li><li>Video Marketing</li><li>Business Cases</li></ul>
  </div>
  <div class="footer-col divided" style="left:563px;width:121px">
    <h4>Services</h4>
    <ul><li>Help/Contact us</li><li>Business directory</li><li>Legal notices</li><li>Privacy policy</li><li>Terms &amp; Conditions</li></ul>
  </div>
  <div class="footer-col" style="left:711px;width:120px">
    <h4>Follow us</h4>
    <div class="social"><span></span><span></span><span></span><span></span></div>
  </div>
</footer>
<p class="copyright">Copyright © 2012 Veriton Communications Company. All rights reserved.</p>

</body>
</html>
```